Halvern Power "Unique Process" Graphic

Create a "graphic" that creatively represents the seven-step process that Halvern Power uses to serve our customers.
This graphic should be sized in such a way that it can easily be included on a page in our website, and also used in other marketing materials such as flyers, emails and powerpoint presentations.
As an EXAMPLE of a similar graphic, see the "Proven Process" section of the home page of this website - https://www.trelvonsite.com/
I'll include our brand documentation as well as the document for our "Unique Process" in the uploaded files section.
Please use our brand colors and also be creative in how you represent the seven steps graphically.
Here's a bit about our business.
Halvern Power is one of the largest B2B Energy Brokers in the US. We serve tens of thousands of customers by securing energy contracts for them. We are NOT an energy company ourselves - but a broker that represents 30+ energy suppliers to commercial and nonprofit customers.

```html
<!DOCTYPE html>
<html lang="en">
<head>
<meta charset="utf-8">
<title>Halvern Power – Unique Process</title>
<link href="https://fonts.googleapis.com/css2?family=Montserrat:ital,wght@0,400;0,600;0,700;0,800;1,800&display=swap" rel="stylesheet">
<style>
  :root {
    --navy: #1d3a6e;
    --green: #0f8f43;
    --ink: #2a2a2a;
    --bg-light: #ffffff;
    --bg-edge: #ececec;
  }
  * { margin: 0; padding: 0; box-sizing: border-box; }
  html, body { width: 1200px; height: 846px; overflow: hidden; }
  body {
    font-family: 'Montserrat', sans-serif;
    background: radial-gradient(ellipse at 50% 50%, var(--bg-light) 40%, var(--bg-edge) 100%);
    position: relative;
    color: var(--ink);
  }
  .brand {
    position: absolute; left: 96px; top: 158px;
    display: flex; align-items: center; gap: 10px;
    font-weight: 800; font-size: 26px; color: var(--navy);
    letter-spacing: 0.5px; text-transform: uppercase;
  }
  .brand-mark { width: 22px; height: 22px; background: var(--green); border-radius: 3px; }
  .process-path { position: absolute; left: 0; top: 0; }
  .step-badge {
    position: absolute; width: 62px; height: 62px;
    transform: translate(-50%, -50%);
  }
  .step-badge::before {
    content: ""; position: absolute; left: 9px; top: 9px;
    width: 44px; height: 44px; background: var(--green);
    border-radius: 9px; transform: rotate(45deg);
  }
  .step-badge svg {
    position: absolute; left: 17px; top: 17px; width: 28px; height: 28px;
    fill: none; stroke: #fff; stroke-width: 1.8; stroke-linecap: round; stroke-linejoin: round;
  }
  .step-text {
    position: absolute; width: 190px; transform: translateX(-50%);
    text-align: center;
  }
  .step-label { font-weight: 600; font-size: 12.5px; color: var(--navy); line-height: 18px; letter-spacing: 0.2px; }
  .step-name { font-weight: 800; font-style: italic; font-size: 14px; color: var(--green); line-height: 19px; letter-spacing: 0.2px; }
  .step-body { font-size: 9.3px; line-height: 12.4px; color: var(--ink); }
  .step-body b { color: var(--navy); font-weight: 600; }
  .step-body.above { margin-bottom: 12px; }
  .step-body.below { margin-top: 8px; }
  .section-title {
    position: absolute; left: 92px; top: 646px;
    display: flex; align-items: center; gap: 4px;
    font-weight: 800; font-size: 46px; color: var(--navy);
  }
  .section-title .rule { width: 50px; height: 4px; background: var(--navy); }
</style>
</head>
<body>

  <div class="brand"><span class="brand-mark"></span>Halvern Power</div>

  <svg class="process-path" width="1200" height="846" viewBox="0 0 1200 846">
    <g fill="none" stroke="#1d3a6e" stroke-width="1.3" stroke-dasharray="3 2.5">
      <path d="M159 232 H232 Q242 232 242 242 V348 Q242 367 261 367 H1032 Q1052 367 1052 387 V492"/>
    </g>
    <g fill="#fff" stroke="#1d3a6e" stroke-width="1.3">
      <rect x="144" y="225" width="14" height="14" transform="rotate(45 151 232)"/>
      <rect x="369" y="360" width="14" height="14" transform="rotate(45 376 367)"/>
      <rect x="504" y="360" width="14" height="14" transform="rotate(45 511 367)"/>
      <rect x="640" y="360" width="14" height="14" transform="rotate(45 647 367)"/>
      <rect x="774" y="360" width="14" height="14" transform="rotate(45 781 367)"/>
      <rect x="909" y="360" width="14" height="14" transform="rotate(45 916 367)"/>
      <rect x="1045" y="496" width="14" height="14" transform="rotate(45 1052 503)"/>
    </g>
  </svg>

  <!-- Step 1: Assessment -->
  <div class="step-badge" style="left:151px;top:285px">
    <svg viewBox="0 0 28 28"><rect x="6" y="5" width="14" height="18" rx="2"/><path d="M10 4h6v3h-6z"/><path d="M9 11h8M9 15h5"/><path d="M15 20l3 3 6-7"/></svg>
  </div>
  <div class="step-text" style="left:151px;top:326px">
    <div class="step-label">HALVERN</div>
    <div class="step-name">ASSESSMENT</div>
    <div class="step-body below">Spend <b>15 minutes</b> with our team while we analyze your account and contract details to <b>select suppliers</b> that fit your needs.</div>
  </div>

  <!-- Step 2: Options -->
  <div class="step-badge" style="left:376px;top:427px">
    <svg viewBox="0 0 28 28"><path d="M5 8h18M5 14h18M5 20h18"/><circle cx="10" cy="8" r="2" fill="#0f8f43"/><circle cx="18" cy="14" r="2" fill="#0f8f43"/><circle cx="12" cy="20" r="2" fill="#0f8f43"/></svg>
  </div>
  <div class="step-text" style="left:376px;top:464px">
    <div class="step-label">HALVERN</div>
    <div class="step-name">OPTIONS!</div>
    <div class="step-body below">options! We'll send you an energy quote with at least <b>three options</b> to choose from - including different suppliers and contract terms. Our <b>unbiased advice</b> will help you find the best solution!</div>
  </div>

  <!-- Step 3: Sign-up -->
  <div class="step-text" style="left:511px;top:195px">
    <div class="step-body above">Our simple sign-up process is handled <b>electronically</b>. Even contract signatures.</div>
    <div class="step-name">SIGN-UP!</div>
    <div class="step-label">HALVERN</div>
  </div>
  <div class="step-badge" style="left:511px;top:311px">
    <svg viewBox="0 0 28 28"><circle cx="12" cy="10" r="4.5"/><path d="M4 23c0-5 4-8 8-8 2 0 3 .4 4 1"/><path d="M20 17v7M16.5 20.5h7"/></svg>
  </div>

  <!-- Step 4: QA -->
  <div class="step-badge" style="left:647px;top:427px">
    <svg viewBox="0 0 28 28"><path d="M8 7l1.5 1.5L12 6M8 12l1.5 1.5L12 11"/><path d="M15 7h6M15 12h6"/><path d="M4 20h5l4 2h6l4-4"/><path d="M4 24h14l6-5"/></svg>
  </div>
  <div class="step-text" style="left:647px;top:464px">
    <div class="step-label">HALVERN</div>
    <div class="step-name">QA</div>
    <div class="step-body below">Every order detail is confirmed to <b>ensure accuracy</b> and smooth processing.</div>
  </div>

  <!-- Step 5: Monitoring -->
  <div class="step-text" style="left:781px;top:171px">
    <div class="step-body above">We <b>proactively monitor</b> your accounts to address any <b>contractual issues</b> with suppliers, should they arise. (E.g., You sell your business, account number changes, etc.)</div>
    <div class="step-name">MONITORING</div>
    <div class="step-label">HALVERN</div>
  </div>
  <div class="step-badge" style="left:781px;top:311px">
    <svg viewBox="0 0 28 28"><rect x="3" y="5" width="22" height="14" rx="1.5"/><path d="M11 23h6M14 19v4"/><path d="M7 15l4-4 3 2 4-4"/><circle cx="19" cy="11" r="3"/><path d="M21 13l2 2"/></svg>
  </div>

  <!-- Step 6: Renewal -->
  <div class="step-badge" style="left:916px;top:427px">
    <svg viewBox="0 0 28 28"><rect x="7" y="4" width="14" height="18" rx="1.5"/><path d="M4 8v16h13"/><path d="M10 9h8M10 13h5"/><circle cx="19" cy="20" r="3.5"/><path d="M21.5 22.5l2 2"/></svg>
  </div>
  <div class="step-text" style="left:916px;top:464px">
    <div class="step-label">HALVERN</div>
    <div class="step-name">RENEWAL</div>
    <div class="step-body below">To protect your business from <b>market volatility</b>, we contact you ahead of your contract end date to discuss renewal options. If anyone else contacts you, you respond, <b>"No thank you, we have Halvern!"</b></div>
  </div>

  <!-- Step 7: Guarantee -->
  <div class="step-badge" style="left:1052px;top:562px">
    <svg viewBox="0 0 28 28"><path d="M14 3l9 3v7c0 6-4 10-9 12-5-2-9-6-9-12V6z"/><path d="M14 7l5 1.7v4.3c0 3.5-2.3 6-5 7.2-2.7-1.2-5-3.7-5-7.2V8.7z"/><path d="M11.5 13.5l2 2 3.5-4"/></svg>
  </div>
  <div class="step-text" style="left:1052px;top:597px">
    <div class="step-label">HALVERN</div>
    <div class="step-name">GUARANTEE</div>
    <div class="step-body below">Sleep Easy! You'll never fall <b>"out of contract"</b> with Halvern as your broker.</div>
  </div>

  <h1 class="section-title"><span class="rule"></span>Unique Process<span class="rule"></span></h1>

</body>
</html>
```